Website - Tides Of Motion

We are catalysts of change in people's lives.
We work with individuals and professionals to bring about instant substantial & transforming change in their lives.
We provide one-on-one lifestyle coaching by an experienced practitioner.
Our existing website is www.tidesofmotion.biz & this site contains our the basis for the content of our desired new project, so please examine this carefully.
We require a professional and captivating website that will instantly impress, engage invite our readers to click & invest their lives.
Our services do not come cheap, but are second to none.
Our website must be contemporary whilst reflecting indisputable class & ultra-confidence in the success of our work.
Target Market(s)
Those who seek to want to change in their lives. Those aged primarily between 30 and 50 years of age, male or female.
Industry/Entity Type
Work

```html
<!DOCTYPE html>
<html lang="en">
<head>
<meta charset="utf-8">
<title>Tides Of Motion</title>
<link href="https://fonts.googleapis.com/css2?family=Jost:wght@300;400;500&display=swap" rel="stylesheet">
<style>
  :root {
    --black: #000000;
    --white: #ffffff;
    --ink: #1e1e1e;
    --grey-text: #8a8a8a;
    --grey-mid: #8c8c8c;
    --grey-dark: #444444;
    --orange: #e8751a;
    --orange-halo: #f8dfcc;
    --teal: #3a9fc0;
    --rust: #e36a1a;
    --green: #4aa53b;
    --sky: #ecd2b4;
    --haze: #f3e6d6;
    --sea: #c2b8aa;
    --sand: #b0916f;
    --sand-dark: #8f7152;
  }
  * { margin: 0; padding: 0; box-sizing: border-box; }
  html, body { width: 1200px; height: 961px; overflow: hidden; background: var(--white); }
  body { position: relative; font-family: "Jost", sans-serif; }

  .site-header { position: absolute; left: 0; top: 0; width: 1200px; height: 100px; background: var(--black); }
  .brand { position: absolute; left: 155px; top: 32px; display: flex; align-items: center; gap: 12px; color: var(--white); font-size: 27px; font-weight: 400; line-height: 1; }
  .brand-mark { width: 26px; height: 26px; background: var(--orange); border-radius: 50%; }
  .main-nav { position: absolute; right: 155px; top: 49px; display: flex; gap: 38px; }
  .main-nav a { color: var(--white); text-decoration: none; font-size: 16px; font-weight: 400; line-height: 22px; }

  .hero { position: absolute; left: 0; top: 100px; width: 1200px; height: 595px; }
  .hero-photo { position: absolute; inset: 0;
    background: linear-gradient(180deg, var(--sky) 0%, var(--haze) 28%, var(--sea) 45%, var(--sand) 70%, var(--sand-dark) 100%); }
  .hero-tagline { position: absolute; left: 537px; top: 240px; color: var(--ink); font-size: 49px; font-weight: 300; line-height: 55px; letter-spacing: -0.3px; }
  .hero-arrow { position: absolute; top: 279px; width: 24px; height: 40px; }
  .hero-arrow.prev { left: 108px; }
  .hero-arrow.next { left: 1070px; }

  .welcome { position: absolute; left: 0; top: 695px; width: 1200px; height: 210px; text-align: center; }
  .welcome-title { margin-top: 20px; font-size: 32px; font-weight: 400; line-height: 42px; color: var(--black); }
  .welcome-title .soft { color: var(--grey-mid); }
  .welcome-title .strong { color: var(--grey-dark); }
  .welcome-text { width: 900px; margin: 14px auto 0; font-family: Arial, Helvetica, sans-serif; font-size: 14px; line-height: 19px; color: var(--grey-text); }
  .learn-more { position: absolute; left: 506px; top: 131px; width: 188px; height: 50px; border-radius: 25px; background: var(--orange-halo); padding: 6px; }
  .learn-more a { display: block; height: 38px; border-radius: 19px; background: var(--orange); color: var(--white); text-decoration: none; font-size: 18px; font-weight: 500; line-height: 38px; letter-spacing: 0.8px; }

  .site-footer { position: absolute; left: 0; top: 905px; width: 1200px; height: 56px; background: var(--black); text-align: center; font-family: Arial, Helvetica, sans-serif; font-size: 12px; line-height: 56px; color: var(--white); }
  .site-footer .tides { color: var(--teal); }
  .site-footer .of { color: var(--rust); }
  .site-footer .motion { color: var(--green); }
</style>
</head>
<body>
  <header class="site-header">
    <div class="brand"><span class="brand-mark"></span>Tides Of Motion</div>
    <nav class="main-nav">
      <a href="#">Home</a>
      <a href="#">Business</a>
      <a href="#">Individual</a>
      <a href="#">Contact Us</a>
    </nav>
  </header>

  <section class="hero">
    <div class="hero-photo" role="img" aria-label="A couple in white clothes walking barefoot along a beach at sunset, waves behind them"></div>
    <svg class="hero-arrow prev" viewBox="0 0 24 40" aria-hidden="true"><polyline points="20,2 3,20 20,38" fill="none" stroke="#ffffff" stroke-width="3"/></svg>
    <h1 class="hero-tagline">We are catalysts of change<br>in people's lives</h1>
    <svg class="hero-arrow next" viewBox="0 0 24 40" aria-hidden="true"><polyline points="4,2 21,20 4,38" fill="none" stroke="#ffffff" stroke-width="3"/></svg>
  </section>

  <section class="welcome">
    <h2 class="welcome-title">Welcome to <span class="soft">Tides Of</span> <span class="strong">Motion</span></h2>
    <p class="welcome-text">Lorem ipsum dolor sit amet, consectetur adipisicing elit. Accusamus, vero, voluptates at temporibus fugit praesentium eaque aspernatur a ipsam non dolor repellendus blanditiis unde eveniet iusto iure voluptatum ad officiis molestiae sit explicabo.</p>
    <div class="learn-more"><a href="#">LEARN MORE</a></div>
  </section>

  <footer class="site-footer">©2002-2013 <span class="tides">Tides</span> <span class="of">Of</span> <span class="motion">Motion</span></footer>
</body>
</html>
```